Design some Business Cards for Brellor Motionworks

Brellor Motionworks, an automation design and services company specializing in packaging equipment in manufacturing facilities is in need of an updated business card design. I've got 3 different variations on the logo which I've attached. The primary hex colors are:

53D41D >> green
666666 >> grey

For the business cards, we'd like a 2-sided card. The info side should include:
- employee name
- title
- company name
- company address (6128 Foundry Lane, York, PA 17408)
- phone (both +1.717.555.0183 and 800.555.0147)
- e-mail

The web address [login to view URL] should appear somewhere on the card but I'll leave it up to you for the placement.

The color green should be highlighted on at least one side of the card. The logo cannot be altered in color or layout from the files provided.

PLEASE LIMIT YOUR SUBMISSIONS TO A MAXIMUM OF 12 DESIGNS.

I look forward to seeing the results.

Thanks in advance,
Mirabel

```html
<!DOCTYPE html>
<html lang="en">
<head>
<meta charset="utf-8">
<title>Brellor Motionworks – Business Card</title>
<link rel="stylesheet" href="https://fonts.googleapis.com/css2?family=Open+Sans:wght@400;600&family=Montserrat:wght@600&display=swap">
<style>
  :root {
    --green: #53d41d;
    --green-dark: #45b316;
    --grey: #666666;
    --ink: #333333;
    --paper: #ffffff;
    --backdrop: #ececec;
  }
  * { box-sizing: border-box; margin: 0; padding: 0; }
  html, body { width: 1200px; height: 800px; overflow: hidden; }
  body {
    background: var(--backdrop);
    font-family: "Open Sans", Arial, sans-serif;
    display: flex;
    align-items: center;
    justify-content: center;
    gap: 60px;
  }
  .card {
    position: relative;
    width: 520px;
    height: 297px;
    background: var(--paper);
    box-shadow: 0 6px 18px rgba(0,0,0,0.12);
    overflow: hidden;
  }
  .card-band {
    position: absolute;
    left: 0; right: 0; bottom: 0;
    height: 34px;
    background: var(--green);
    color: var(--paper);
    font-size: 13px;
    display: flex;
    align-items: center;
    padding: 0 22px;
  }
  /* Front: logo side */
  .card-front .brand {
    position: absolute;
    top: 0; left: 0; right: 0; bottom: 34px;
    display: flex;
    align-items: center;
    justify-content: center;
    gap: 14px;
  }
  .brand-dot {
    width: 54px; height: 54px;
    border-radius: 50%;
    background: var(--green);
    flex: none;
  }
  .brand-name {
    font-family: "Montserrat", Arial, sans-serif;
    font-weight: 600;
    font-size: 30px;
    color: var(--green);
    letter-spacing: 0.5px;
  }
  .card-front .card-band { justify-content: flex-end; }
  /* Back: info side */
  .card-back .info-body {
    position: absolute;
    top: 0; left: 0; right: 0; bottom: 34px;
    display: flex;
    align-items: center;
    padding: 0 40px 0 48px;
    gap: 40px;
  }
  .company-mark {
    display: flex;
    flex-direction: column;
    align-items: center;
    gap: 10px;
    width: 150px;
  }
  .company-mark .brand-dot { width: 96px; height: 96px; }
  .company-mark .company-name {
    font-family: "Montserrat", Arial, sans-serif;
    font-weight: 600;
    font-size: 13px;
    color: var(--grey);
    text-align: center;
  }
  .person-name { font-size: 19px; font-weight: 600; color: var(--ink); }
  .person-title { font-size: 13px; color: var(--green); margin-bottom: 14px; }
  .contact-list { list-style: none; }
  .contact-list li {
    display: flex;
    align-items: center;
    gap: 8px;
    font-size: 13px;
    color: var(--ink);
    line-height: 21px;
  }
  .contact-list svg { width: 12px; height: 12px; flex: none; }
  .card-back .card-band { justify-content: center; }
</style>
</head>
<body>
  <section class="card card-front">
    <div class="brand">
      <span class="brand-dot"></span>
      <span class="brand-name">Brellor Motionworks</span>
    </div>
    <div class="card-band">www.brellormotionworks.com</div>
  </section>

  <section class="card card-back">
    <div class="info-body">
      <div class="company-mark">
        <span class="brand-dot"></span>
        <span class="company-name">Brellor Motionworks</span>
      </div>
      <div class="person">
        <p class="person-name">Dana Whitley</p>
        <p class="person-title">Manager</p>
        <ul class="contact-list">
          <li>
            <svg viewBox="0 0 12 12" aria-hidden="true"><path d="M2.5 1 L4.5 1 L5.2 3.4 L4 4.4 C4.6 5.8 6.2 7.4 7.6 8 L8.6 6.8 L11 7.5 L11 9.5 C11 10.3 10.3 11 9.5 11 C5 11 1 7 1 2.5 C1 1.7 1.7 1 2.5 1 Z" fill="var(--green)"/></svg>
            +1.717.555.0183
          </li>
          <li>
            <svg viewBox="0 0 12 12" aria-hidden="true"><path d="M2.5 1 L4.5 1 L5.2 3.4 L4 4.4 C4.6 5.8 6.2 7.4 7.6 8 L8.6 6.8 L11 7.5 L11 9.5 C11 10.3 10.3 11 9.5 11 C5 11 1 7 1 2.5 C1 1.7 1.7 1 2.5 1 Z" fill="var(--green)"/></svg>
            800.555.0147
          </li>
          <li>
            <svg viewBox="0 0 12 12" aria-hidden="true"><rect x="1" y="2.5" width="10" height="7" rx="1" fill="var(--green)"/><path d="M1.5 3 L6 6.5 L10.5 3" stroke="#fff" stroke-width="1" fill="none"/></svg>
            info@brellormotionworks.com
          </li>
          <li>
            <svg viewBox="0 0 12 12" aria-hidden="true"><circle cx="6" cy="6" r="5" fill="var(--green)"/><path d="M1 6 H11 M6 1 C3.5 3.5 3.5 8.5 6 11 M6 1 C8.5 3.5 8.5 8.5 6 11" stroke="#fff" stroke-width="0.8" fill="none"/></svg>
            www.brellormotionworks.com
          </li>
        </ul>
      </div>
    </div>
    <div class="card-band">6128 Foundry Lane, York, PA 17408</div>
  </section>
</body>
</html>
```